Website for Larkwood Fresh Foods

Slogan to be used is Fresh is Best !
I would like the website to be like my other business @ www.tuberhaven.com.au. It is the same business

Industry/Entity Type

Vegetable Processing

Coding

Coded - Design and coding required

Number of Pages Required

1 page

```html
<!DOCTYPE html>
<html lang="en">
<head>
<meta charset="utf-8">
<title>Larkwood Fresh Foods – Fresh is Best!</title>
<link href="https://fonts.googleapis.com/css2?family=Montserrat:wght@400;500;600;700;800&family=Arimo:wght@400;700&family=Lobster&display=swap" rel="stylesheet">
<style>
:root{
  --lime:#94bd2c;
  --lime-dark:#7fa51f;
  --lime-pale:#c3dd84;
  --forest:#1d6b12;
  --forest-deep:#175a0c;
  --btn:#257d14;
  --ink:#111;
  --grey:#555;
  --mist:#f0f0f4;
  --white:#fff;
}
*{box-sizing:border-box;margin:0;padding:0}
html,body{width:1200px;height:3264px;overflow:hidden}
body{position:relative;background:var(--white);font-family:"Arimo",Arial,sans-serif;color:var(--ink)}
.abs{position:absolute}
.mont{font-family:"Montserrat",Arial,sans-serif}

/* header */
.callbar{left:678px;top:0;width:522px;height:46px;background:var(--lime);clip-path:polygon(0 0,100% 0,100% 100%,28px 100%);color:var(--white);font:700 20px "Montserrat",sans-serif;letter-spacing:.5px;display:flex;align-items:center;padding-left:62px}
.logo{left:151px;top:64px;font:800 27px "Montserrat",sans-serif;color:var(--btn);letter-spacing:.3px}
.nav{left:418px;top:70px;display:flex;gap:38px;font:600 17px "Montserrat",sans-serif;color:#222}
.nav .active{color:var(--btn)}
.burger{left:1024px;top:68px;width:26px}
.burger span{display:block;height:3px;background:#222;margin-bottom:6px;border-radius:2px}

/* hero */
.hero{left:0;top:117px;width:1200px;height:399px;background:linear-gradient(90deg,#3d5a26 0%,#5e7d33 30%,#8fb03a 55%,#c9dc6a 72%,#6f9a2a 100%)}
.hero-title{left:676px;top:236px;font:400 68px "Lobster",cursive;color:var(--white);text-shadow:0 3px 6px rgba(0,0,0,.25)}
.btn-outline{border:3px solid var(--white);border-radius:30px;color:var(--white);font:700 18px "Montserrat",sans-serif;display:flex;align-items:center;justify-content:center;letter-spacing:.5px}
.hero-btn{left:668px;top:331px;width:165px;height:47px;background:var(--lime)}

/* products */
.deliver{left:0;top:516px;width:1200px;height:760px;background:var(--mist)}
.eyebrow{left:0;width:1200px;top:586px;text-align:center;font:600 23px "Montserrat",sans-serif;color:#555}
.section-title{left:0;width:1200px;text-align:center;font:700 44px "Montserrat",sans-serif}
.lead{left:190px;width:820px;top:688px;text-align:center;font-size:13.2px;line-height:19px;color:#222}
.card{top:800px;width:208px;height:245px;background:var(--white);border-radius:26px;box-shadow:0 4px 14px rgba(0,0,0,.05);text-align:center}
.card .thumb{position:absolute;left:49px;top:-42px;width:109px;height:109px;border-radius:50%}
.card h3{position:absolute;top:101px;width:100%;font:700 17px "Montserrat",sans-serif;color:var(--btn)}
.card p{position:absolute;top:129px;left:20px;width:168px;font-size:11px;line-height:15px;color:#333}
.btn-solid{background:var(--btn);color:var(--white);border-radius:20px;font:700 12px "Montserrat",sans-serif;display:flex;align-items:center;justify-content:center;letter-spacing:.4px}
.card .btn-solid{position:absolute;left:48px;top:188px;width:111px;height:29px}
.arrow{width:32px;height:32px;border-radius:50%;background:#8a8a8a}

/* about */
.about-photo{left:175px;top:1420px;width:410px;height:410px;border-radius:50%;background:radial-gradient(circle at 50% 40%,#c98a4c 0%,#7a5a3c 45%,#4a6aa0 75%,#6f8e3e 100%)}
.about-ring{left:145px;top:1390px;width:470px;height:470px;border-radius:50%;border:3px dotted rgba(255,255,255,.75)}
.about-title{left:678px;top:1452px;font:700 44px "Montserrat",sans-serif;color:var(--white)}
.about-text{left:678px;top:1525px;width:375px;font-size:11px;line-height:16.3px;color:var(--white)}
.about-btn{left:678px;top:1737px;width:155px;height:44px;font-size:17px}

/* customers */
.cust-title{top:2113px;font-size:48px;font-weight:800}
.cust h4{font:700 16px "Montserrat",sans-serif;margin-bottom:6px}
.cust p{font-size:11.5px;line-height:15px;color:#444}
.cust.left{text-align:right;width:210px}
.cust.right{width:210px}
.cust-icon{width:80px;height:80px;border-radius:50%;background:var(--btn);display:flex;align-items:center;justify-content:center}
.produce{left:462px;top:2226px;width:312px;height:200px;border-radius:50%/42%;background:radial-gradient(ellipse at 50% 55%,#c69a5a 0%,#b9812f 30%,#d9382a 55%,#6aa032 75%,rgba(255,255,255,0) 78%)}
.view-btn{left:524px;top:2470px;width:152px;height:42px;border-radius:22px;font-size:16px}

/* call to action + footer */
.cta{left:176px;top:2638px;width:850px;height:168px;background:var(--lime);border-radius:84px;box-shadow:4px 4px 0 var(--white),6px 6px 0 rgba(0,0,0,.03);text-align:center;color:var(--white)}
.cta .big{margin-top:40px;font:700 46px "Montserrat",sans-serif}
.cta .small{margin-top:-4px;font:700 20px "Montserrat",sans-serif}
.foot-h{top:2968px;font:700 21px "Montserrat",sans-serif;color:var(--white)}
.foot-t{font:400 14px "Montserrat",sans-serif;color:var(--white);line-height:22px}
.rule{left:158px;top:3168px;width:905px;height:1px;background:rgba(255,255,255,.35)}
.copy{left:0;width:1200px;top:3206px;text-align:center;font:400 13px "Montserrat",sans-serif;color:var(--white)}
.social{width:30px;height:30px;border-radius:50%;background:var(--lime)}
</style>
</head>
<body>

<div class="abs callbar">CALL US NOW: 02 5550 1234</div>
<div class="abs logo">LARKWOOD</div>
<nav class="abs nav"><span class="active">Home</span><span>About</span><span>Our Customers</span><span>Our Menu</span><span>Contact</span></nav>
<div class="abs burger"><span></span><span></span><span></span></div>

<div class="abs hero" role="img" aria-label="Person holding a wooden crate of fresh vegetables in a green field"></div>
<div class="abs hero-title">Fresh is Best!</div>
<div class="abs btn-outline hero-btn">ORDER NOW</div>

<section class="abs deliver"></section>
<div class="abs eyebrow">We Deliver</div>
<h2 class="abs section-title" style="top:614px">Fresh, Quality Products</h2>
<p class="abs lead">Lorem ipsum dolor sit amet, consectetur adipiscing elit, sed do eiusmod tempor incididunt ut labore et dolore magna aliqua. Ut enim ad minim veniam, quis nostrud exercitation ullamco laboris nisi ut aliquip ex ea commodo consequat.</p>

<div class="abs arrow" style="left:54px;top:890px"><svg width="32" height="32" viewBox="0 0 32 32"><path d="M23 16H10M15 10l-6 6 6 6" stroke="#fff" stroke-width="3.5" fill="none" stroke-linecap="round" stroke-linejoin="round"/></svg></div>
<div class="abs arrow" style="left:1113px;top:896px"><svg width="32" height="32" viewBox="0 0 32 32"><path d="M9 16h13M17 10l6 6-6 6" stroke="#fff" stroke-width="3.5" fill="none" stroke-linecap="round" stroke-linejoin="round"/></svg></div>

<div class="abs card" style="left:151px"><div class="thumb" role="img" aria-label="Potatoes" style="background:radial-gradient(circle,#e2b45a,#8a5a2a)"></div><h3>POTATOES</h3><p>Lorem ipsum dolor sit amet, consectetur adipiscing elit, sed labore et aliqua.</p><div class="btn-solid">READ MORE</div></div>
<div class="abs card" style="left:380px"><div class="thumb" role="img" aria-label="Pumpkins" style="background:radial-gradient(circle,#f08a2a,#7a3a12)"></div><h3>PUMPKIN</h3><p>Lorem ipsum dolor sit amet, consectetur adipiscing elit, sed labore et aliqua.</p><div class="btn-solid">READ MORE</div></div>
<div class="abs card" style="left:610px"><div class="thumb" role="img" aria-label="Carrots" style="background:radial-gradient(circle,#f07a22,#3e6a22)"></div><h3>CARROT</h3><p>Lorem ipsum dolor sit amet, consectetur adipiscing elit, sed labore et aliqua.</p><div class="btn-solid">READ MORE</div></div>
<div class="abs card" style="left:839px"><div class="thumb" role="img" aria-label="Cabbages" style="background:radial-gradient(circle,#c6e0a0,#2f5a2a)"></div><h3>CABBAGE</h3><p>Lorem ipsum dolor sit amet, consectetur adipiscing elit, sed labore et aliqua.</p><div class="btn-solid">READ MORE</div></div>

<svg class="abs" style="left:0;top:1180px" width="1200" height="880" viewBox="0 0 1200 880">
  <circle cx="990" cy="758" r="148" fill="var(--lime-pale)"/>
  <path d="M0,45 C180,40 260,80 370,40 C460,5 560,-10 700,30 C820,70 880,105 980,80 C1080,55 1150,30 1200,18 L1200,745 C1000,740 800,745 600,790 C450,820 300,810 180,770 C100,745 40,720 0,708 Z" fill="var(--lime-dark)"/>
  <path d="M0,80 C180,75 260,115 370,80 C460,48 560,35 700,68 C820,100 890,135 990,110 C1090,85 1150,65 1200,55 L1200,745 C1000,740 800,745 600,790 C450,820 300,810 180,770 C100,745 40,720 0,708 Z" fill="var(--lime)"/>
</svg>
<div class="abs about-ring"></div>
<div class="abs about-photo" role="img" aria-label="Smiling grocer in an apron holding a crate of vegetables in a market"></div>
<h2 class="abs about-title">ABOUT US</h2>
<p class="abs about-text">Lorem ipsum dolor sit amet, consectetur adipiscing elit, sed do eiusmod tempor incididunt ut labore et dolore magna aliqua. Ut enim ad minim veniam, quis nostrud exercitation ullamco laboris nisi ut aliquip ex ea commodo consequat. Duis aute irure dolor in reprehenderit in voluptate velit esse cillum dolore eu fugiat nulla pariatur. Excepteur sint occaecat cupidatat non proident, sunt in culpa qui officia deserunt mollit anim id est laborum. Sed ut perspiciatis unde omnis iste natus error sit voluptatem accusantium doloremque laudantium, totam rem aperiam, eaque ipsa quae ab illo inventore veritatis et quasi architecto beatae vitae dicta sunt explicabo. sed quia consequuntur magni dolores eos qui ratione voluptatem sequi nesciunt.</p>
<div class="abs btn-outline about-btn">READ MORE</div>

<h2 class="abs section-title cust-title">CUSTOMERS</h2>

<div class="abs cust left" style="left:145px;top:2230px"><h4>HOSPITAL</h4><p>Lorem ipsum dolor sit amet, conse adipiscing el dolor sit aliqua.</p></div>
<div class="abs cust-icon" style="left:370px;top:2220px"><svg width="44" height="44" viewBox="0 0 44 44" fill="#fff"><rect x="8" y="8" width="28" height="34"/><rect x="3" y="20" width="6" height="22"/><rect x="35" y="20" width="6" height="22"/><g fill="var(--btn)"><rect x="20" y="11" width="4" height="10"/><rect x="17" y="14" width="10" height="4"/><rect x="12" y="25" width="4" height="4"/><rect x="20" y="25" width="4" height="4"/><rect x="28" y="25" width="4" height="4"/><rect x="18" y="33" width="8" height="9"/></g></svg></div>
<div class="abs cust left" style="left:145px;top:2348px"><h4>NURSING HOMES</h4><p>Lorem ipsum dolor sit amet, conse adipiscing el dolor sit aliqua.</p></div>
<div class="abs cust-icon" style="left:370px;top:2340px"><svg width="44" height="44" viewBox="0 0 44 44" fill="none" stroke="#fff" stroke-width="3.5" stroke-linejoin="round"><path d="M4,22 22,6 40,22M9,18v20h26V18"/><path d="M22,34c-7-5-8-8-5-10 2-1 4 0 5 2 1-2 3-3 5-2 3 2 2 5-5 10z" fill="#fff" stroke="none"/></svg></div>

<div class="abs produce" role="img" aria-label="Wooden crate surrounded by assorted fruit and vegetables"></div>

<div class="abs cust-icon" style="left:777px;top:2220px"><svg width="44" height="44" viewBox="0 0 44 44" fill="#fff"><path d="M6,16 22,6 38,16Z"/><rect x="10" y="18" width="24" height="4"/><rect x="4" y="24" width="36" height="18"/><g fill="var(--btn)"><rect x="9" y="30" width="5" height="12"/><rect x="19" y="30" width="6" height="12"/><rect x="30" y="30" width="5" height="12"/></g></svg></div>
<div class="abs cust right" style="left:875px;top:2230px"><h4>CLUBS</h4><p>Lorem ipsum dolor sit amet, conse adipiscing el dolor sit aliqua.</p></div>
<div class="abs cust-icon" style="left:777px;top:2340px"><svg width="44" height="44" viewBox="0 0 44 44" fill="#fff"><circle cx="22" cy="5" r="2.5"/><circle cx="14" cy="8" r="2"/><circle cx="30" cy="8" r="2"/><rect x="13" y="13" width="18" height="29"/><rect x="5" y="24" width="8" height="18"/><rect x="31" y="24" width="8" height="18"/><g fill="var(--btn)"><rect x="17" y="17" width="4" height="4"/><rect x="23" y="17" width="4" height="4"/><rect x="17" y="25" width="4" height="4"/><rect x="23" y="25" width="4" height="4"/><rect x="19" y="34" width="6" height="8"/></g></svg></div>
<div class="abs cust right" style="left:875px;top:2348px"><h4>HOTELS</h4><p>Lorem ipsum dolor sit amet, conse adipiscing el dolor sit aliqua.</p></div>

<div class="abs btn-solid view-btn">VIEW MORE</div>

<svg class="abs" style="left:0;top:2620px" width="1200" height="644" viewBox="0 0 1200 644">
  <path d="M0,70 C200,190 500,220 820,150 C1000,110 1120,80 1200,60 L1200,644 L0,644 Z" fill="var(--lime)"/>
  <path d="M0,150 C220,250 520,260 820,200 C1000,160 1120,120 1200,110 L1200,644 L0,644 Z" fill="var(--forest)"/>
  <path d="M980,30 C1080,40 1150,70 1200,110 L1200,160 C1120,170 1040,140 980,100 Z" fill="var(--forest)"/>
</svg>
<div class="abs cta"><div class="big">Call us now. 02 5550 1234</div><div class="small">you can place your order over the phone. easy!</div></div>

<h4 class="abs foot-h" style="left:151px">COMAPNY</h4>
<p class="abs foot-t" style="left:153px;top:3020px;width:240px;line-height:19px;font-size:13.5px">Lorem ipsum dolor sit ame lohmr consectetur adipiscing elit, sedh do eiusmod tempor incididunt ut labore et dolore magnaua.</p>
<h4 class="abs foot-h" style="left:427px">MENU</h4>
<p class="abs foot-t" style="left:432px;top:3013px">Home<br>About Us<br>Categories<br>Contact Us</p>
<h4 class="abs foot-h" style="left:608px">LINKS</h4>
<p class="abs foot-t" style="left:613px;top:3013px">potatoes<br>pumpkin<br>carrot<br>onion<br>cabbage</p>
<p class="abs foot-t" style="left:720px;top:3013px">celery<br>capsicum<br>zucchini<br>mushroom</p>
<h4 class="abs foot-h" style="left:887px">CONTACT</h4>
<svg class="abs" style="left:886px;top:3018px" width="14" height="16" viewBox="0 0 14 16"><path d="M7,0C3,0 1,3 1,6c0,4 6,10 6,10s6-6 6-10C13,3 11,0 7,0z" fill="var(--lime)"/><circle cx="7" cy="6" r="2.2" fill="var(--forest)"/></svg>
<p class="abs foot-t" style="left:907px;top:3013px;line-height:17px">48 Orchard Lane,<br>Larkwood NSW 2530</p>
<svg class="abs" style="left:885px;top:3067px" width="15" height="15" viewBox="0 0 24 24"><path d="M6.6 10.8a15 15 0 0 0 6.6 6.6l2.2-2.2c.3-.3.7-.4 1-.2 1.1.4 2.3.6 3.6.6.6 0 1 .4 1 1V20c0 .6-.4 1-1 1A17 17 0 0 1 3 4c0-.6.4-1 1-1h3.5c.6 0 1 .4 1 1 0 1.3.2 2.5.6 3.6.1.3 0 .7-.2 1z" fill="var(--lime)"/></svg>
<p class="abs foot-t" style="left:907px;top:3064px">Ph: 02 5550 1235</p>
<svg class="abs" style="left:886px;top:3102px" width="14" height="14" viewBox="0 0 14 14"><rect x="0" y="4" width="14" height="10" rx="1" fill="var(--lime)"/><rect x="3" y="0" width="8" height="5" fill="var(--lime)"/><rect x="3" y="7" width="8" height="2" fill="var(--forest)"/></svg>
<p class="abs foot-t" style="left:907px;top:3099px">Fax: 02 5550 1236</p>

<div class="abs rule"></div>
<p class="abs copy">2023 © Copyright &nbsp;All Rights Reserved.</p>
<div class="abs social" style="left:920px;top:3198px"></div>
<div class="abs social" style="left:957px;top:3198px"></div>
<div class="abs social" style="left:995px;top:3198px"></div>

</body>
</html>
```